Catalogue 2-Page Cover Design

We are a U.S. company that makes and sells functional glass art products. All of our product are hand blown by our artisans. We need your talents and skills to help us make the cover pages of our 2014 catalogue. 2 pages, front (cover 1)and back(cover 2). Here to make things easier we calll it cover 1 and cover 2. Cover 2 should be designed upside down because we need it to be the front page when you flip the catalogue and start reading from the end. This is for the year 2014 so put "2014" on both Cover 1 and Cover 2 please.
The Cover 1 and Cover 2 won't be showing similar content because the "two front pages" lead you to different part of content.
The spine of the book will be 1.5 inch (1.5 inch thick). We need this part to be designed sharp and can pop up on a book shelf from all other books. Our company name should be on it. It can be colorful but no product pics.
Here is what we would want for Cover1 and 2 section:
COVER 1: cover 1 should artisticly present four categories products: Lighting, Wall art Plate, Table Top, and Chandeliers(the curily glass one). Please use pics attached in your design(named under Cover 1-abcd).
COVER2: This cover lead our readers to the contract/project section of the catalogue. We produce custom fixtures and really want to expand our market for the product. We want to draw in designers and customers that are looking for larger-scale lighting product. The cover need to instantly convey a high-end, luxurious but chic installation site.Please use the pic attached under name Cover 2-a in your design. Please convey our CAPABILITY of turning concept and design into real product. One way we are looking at is a mix of the sketch or drawing and the real product. (expample: left side pencil/pen sketch-right side real chandelier.) Please use the product in the pic attached (under name Cover 2-a) in your design. You can use PS to take the product out and put it into any background or settings you like.
We don't want to make very specific and detailed guidlines for that will limit your creativity. We are a pioneer glass art manufacture which breathed new life into a traditional art form. Please show your creativity and make a elegant but cool cover.
Attached files-
1. Catalogue inter pages examples-for a better understanding of our product and this catalogue, to better match the covers with inner pages.
2. Product pictures (Named Cover 1- a,b, c, d and Cover 2-a) - use those pics for your design.
3. Logo-The high res logo pic is also attached. should be put what ever most suitable in your design.
***A4 PAPER***
***Due Date is Monday, Jan 20th ***
Thanks for your time and effort in paticipating in this contest. We welcome any comments and questions.
Target Market(s)
our customers are: Interior Designers, Furnishing Stores, Hotels and Resorts, Art Galleris, Art Museums, Home and Decor Department Stores.
Industry/Entity Type
It Company
Requirements
Must have
- our company info, logo(attached) and other info below:
Tamri Glass Inc.
Corporate Office
3471 Marrow Park Lane, Castelby, CA 94862
Tel: 510-742-3160
Fax:510-742-3168
Email: info@orlencrystalworks.example
Website: www.orlencrystalworks.example
Nice to have
- Be artistic, be special and be cool.
Should not have
- Pictures not related to our company info and products.
Please use only Cover 1-a,b,c,d and Cover 2-a for your design. All other pics are inner page samples to give you a feel of our catalogue.

```html
<!DOCTYPE html>
<html lang="en">
<head>
<meta charset="utf-8">
<title>Tamri Glass Inc. – Catalogue Spine Options</title>
<link href="https://fonts.googleapis.com/css2?family=Roboto:wght@100;300;400&display=swap" rel="stylesheet">
<style>
  :root {
    --page: #ffffff;
    --ink: #111111;
    --frame: #1a1a1a;
    --name-grey: #6f6f6f;
    --brand-blue: #1a9fd8;
    --mist: #f1f3f5;
    --teal: #3fb7b0;
    --amber: #f2a132;
    --rust: #a8361c;
    --maroon: #5a1c14;
    --vase-red: #b8281e;
  }
  * { margin: 0; padding: 0; box-sizing: border-box; }
  html, body { width: 1200px; height: 998px; overflow: hidden; background: var(--page); }
  body { position: relative; font-family: "Roboto", Arial, sans-serif; color: var(--ink); }

  .sheet-title {
    position: absolute; left: 310px; top: 83px;
    font-size: 21px; font-weight: 400; letter-spacing: 0.3px; color: #000;
  }
  .spine {
    position: absolute; top: 123px; width: 100px; height: 766px;
    border: 1px solid var(--frame); overflow: hidden; background: var(--page);
  }
  .spine--three { left: 301px; }
  .spine--four  { left: 543px; width: 98px; background: linear-gradient(180deg, #f6f7f8 0%, var(--mist) 60%, #f7f8f9 100%); }
  .spine--five  { left: 782px; top: 125px; width: 99px; height: 762px; }

  .option-label {
    position: absolute; top: 904px; width: 160px; text-align: center;
    font-size: 22px; font-weight: 400; letter-spacing: 0; color: #000;
  }
  .option-label--three { left: 270px; }
  .option-label--four  { left: 508px; }
  .option-label--five  { left: 751px; }

  .company-name {
    position: absolute; writing-mode: vertical-rl; transform: rotate(180deg);
    font-weight: 100; font-size: 32px; line-height: 1; color: var(--name-grey);
    white-space: nowrap; letter-spacing: 0.3px;
  }
  .spine--three .company-name { left: 36px; top: 150px; }
  .spine--four .company-name  { left: 34px; top: 357px; }

  .brand-mark { display: flex; flex-direction: column; align-items: center; gap: 5px; }
  .brand-mark__dot { width: 14px; height: 14px; border-radius: 50%; background: var(--brand-blue); }
  .brand-mark__name { font-size: 10px; font-weight: 400; color: var(--brand-blue); white-space: nowrap; }

  .spine--three .brand-mark { position: absolute; left: 0; right: 0; top: 38px; }

  .badge {
    position: absolute; border-radius: 50%; background: var(--page);
    display: flex; align-items: center; justify-content: center;
  }
  .spine--four .badge { width: 104px; height: 104px; left: -3px; top: 614px; }
  .spine--five .badge { width: 118px; height: 118px; left: -10px; top: 315px; }

  .product-photo { position: absolute; }
  .spine--three .product-photo {
    left: 0; right: 0; top: 435px; bottom: 0;
    background:
      radial-gradient(ellipse 45% 28% at 50% 80%, var(--vase-red) 0%, #7a2a40 55%, transparent 75%),
      linear-gradient(180deg, #ffffff 0%, #ffffff 55%, #f1f1f1 100%);
  }
  .photo-caption { position: absolute; right: 6px; bottom: 2px; font-size: 5px; color: #555; }
  .spine--four .product-photo {
    left: 0; right: 0; top: 0; height: 320px;
    background: radial-gradient(ellipse 75% 55% at 40% 25%, var(--teal) 0%, rgba(63,183,176,0.55) 45%, rgba(241,243,245,0) 80%);
  }
  .spine--five .product-photo {
    inset: 0;
    background:
      radial-gradient(ellipse 60% 25% at 50% 15%, rgba(150,140,140,0.85) 0%, transparent 70%),
      radial-gradient(ellipse 80% 30% at 40% 35%, var(--rust) 0%, transparent 80%),
      radial-gradient(ellipse 80% 30% at 45% 78%, var(--maroon) 0%, transparent 80%),
      linear-gradient(180deg, var(--amber) 0%, #e0702a 40%, var(--amber) 70%, #e8862c 100%);
  }
</style>
</head>
<body>
  <div class="sheet-title">SPINES</div>

  <section class="spine spine--three">
    <div class="brand-mark">
      <span class="brand-mark__dot"></span>
      <span class="brand-mark__name">Tamri Glass</span>
    </div>
    <div class="company-name">Tamri Glass Inc.</div>
    <div class="product-photo" role="img" aria-label="Multicoloured hand-blown glass vase with a long curling red and blue neck on white">
      <span class="photo-caption">Model 110</span>
    </div>
  </section>

  <section class="spine spine--four">
    <div class="product-photo" role="img" aria-label="Splash of teal hand-blown glass against a pale grey backdrop"></div>
    <div class="company-name">Tamri Glass Inc.</div>
    <div class="badge">
      <div class="brand-mark">
        <span class="brand-mark__dot"></span>
        <span class="brand-mark__name">Tamri Glass</span>
      </div>
    </div>
  </section>

  <section class="spine spine--five">
    <div class="product-photo" role="img" aria-label="Close-up of swirling amber, rust and maroon striped glass"></div>
    <div class="badge">
      <div class="brand-mark">
        <span class="brand-mark__dot"></span>
        <span class="brand-mark__name">Tamri Glass</span>
      </div>
    </div>
  </section>

  <div class="option-label option-label--three">OPTION 3</div>
  <div class="option-label option-label--four">OPTION 4</div>
  <div class="option-label option-label--five">OPTION 5</div>
</body>
</html>
```